Corporate Financial Services

This is a new Company. The ROW represents my son's and my own Christian name initials (ROW) (Colin and Brent) but no real significance.
This is a boutique financial services company active in the full parameter of corporate and business transactions. From standard financial and tax services to specialised Research & Development, mergers and acquisitions, business valuations, and capital raising.
Over 30 years of experience with listed and private entities.
I am after something exciting, given the nature of the business, bright, clean and colourful, but not in comic form.
Hi there,
Firstly thankyou for accepting the challenge. I have no ideas and nothing to compare your submissions with other than other peoples cards.
A few points
I omitted the ABN number from the card description. This is an important reference for all businesses operating in Australia. Therefore the following should be shown in association with the company name ROW Corporate & Financial Services Pty Ltd It can either be within brackets or without but always shown underneath the company name in smaller font.
The eight core business services need to be shown on the reverse
My contact number should also be shown along side the address
My business title is Chartered Accountant in full. I am also not fussed as to whether my name appears in caps or Caps and lowercase ie Brent Ashdown or BRENT ASHDOWN but this will depend upon the design of the rest of the card.
Maybe a small logo for the company needs to be attached but not sure.
Kind regards
Brent Ashdown
Financial
ROW Corporate & Financial Services Pty Ltd
(ABN 71 309 482 157)
(Note ABN could be shown on the reverse side with just ROW Corporate & Financial Services Pty Ltd on the front....no ABN
17 Wattlebank Street Norvale SA 5174
Brent Ashdown
Chartered Accountant
Phone (symbol preferred) +61 (0) 437 215604
Email (symbol) to be provided
www.rowfinsvc-example.com.au
Skype brent7312
- On the reverse:
Corporate Finance
Taxation
Research & Development Specialisation
Financial Accounting
Mergers & Acquisitions
Company Listings (IPO's)
Business Valuations
Capital Raising
- Interested in a strong black card (or grey white platinum and black colours) with either platinum or gold highlight modern name style no italics. I would also like at a later stage with the winner to use this same design for card for Asia with a red and or gold and platinum colour. But I want this batch first.
The smart block (square) for digital image transfer to mobile phones contained within a gold or platinum square border on reverse of the card
Anything old or staid looking. No italics sans serif

```html
<!DOCTYPE html>
<html lang="en">
<head>
<meta charset="utf-8">
<title>ROW Corporate &amp; Financial Services – Business Card</title>
<link href="https://fonts.googleapis.com/css2?family=EB+Garamond:wght@400&family=Source+Sans+3:wght@400&display=swap" rel="stylesheet">
<style>
  :root {
    --backdrop: #2c3739;
    --card-blue: #34a6f0;
    --card-edge: #3b8cc4;
    --text-light: #ffffff;
    --text-dark: #111417;
  }
  html, body {
    margin: 0;
    padding: 0;
    width: 1200px;
    height: 741px;
    overflow: hidden;
    background: var(--backdrop);
  }
  .card {
    position: absolute;
    left: 41px;
    top: 42px;
    width: 1120px;
    height: 658px;
    box-sizing: border-box;
    background: var(--card-blue);
    border: 1px solid var(--card-edge);
  }
  .brand {
    position: absolute;
    left: 0;
    right: 0;
    top: 128px;
    text-align: center;
    color: var(--text-light);
    font-family: "EB Garamond", Georgia, serif;
    font-weight: 400;
  }
  .brand-name {
    margin: 0;
    font-size: 172px;
    line-height: 1;
    letter-spacing: 2px;
  }
  .brand-tagline {
    margin: 22px 0 0;
    font-size: 55px;
    line-height: 1;
    letter-spacing: 0.5px;
  }
  .contact-line {
    position: absolute;
    left: 18px;
    right: 28px;
    top: 571px;
    display: flex;
    justify-content: space-between;
    align-items: baseline;
    margin: 0;
    padding: 0;
    list-style: none;
    font-family: "Source Sans 3", "Myriad Pro", Arial, sans-serif;
    font-size: 22px;
    color: var(--text-dark);
    text-shadow: 1px 1px 1px rgba(255, 255, 255, 0.35);
    white-space: nowrap;
  }
</style>
</head>
<body>
  <main class="card">
    <header class="brand">
      <h1 class="brand-name">ROW</h1>
      <p class="brand-tagline">Corporate &amp; Financial Services</p>
    </header>
    <ul class="contact-line">
      <li class="contact-phone">+61 (0) 437 215604</li>
      <li class="contact-address">no ABN 17 Wattlebank Street Norvale SA 5174 Brent Ashdown</li>
      <li class="contact-web">www.rowfinsvc-example.com</li>
    </ul>
  </main>
</body>
</html>
```